Harbourline Shelter Needs a Tent Canopy and Wall

I need a tent canopy for my detailing company. The company logo, the tent requirements and what I am imagining can be found in the files below. Speed is my main concern so the FIRST person to produce a QUALITY canopy will end up getting my business.

The canopy and wall are going to be red. I want the triangle portion of the canopy to have the company logo in the center of it. Either you can have the company logo on a red background (may need to change the maple leaf of the logo to white) or you can have the company logo as is and somehow incorporate some white into it so that it looks nice. I want a white or black maple leaf at the top of the triangle canopy section on all four sides.

On the rectangular portion right below the triangular section, I want the company name which is MARVELLO DETAILING INC. and the ZELPA and BRELLANTIX logos in all four corners and all four sides. I would prefer the ZELPA and BRELLANTIX logos to be white on the red background.

On the halfwall, I want "Detailing" in the top left corner and "Starting at:" to be right below it in half the size. Then below that I want a very big "$29.95". I want a different color background to encapsulate the 29.95 and I would like the .95 to be smaller than the 29. On the right hand side I would like a "We do house calls" in the top right corner. Below that I would like a bullet point that says "Stain removal", below that "Rug Shampooing" and "Eliminate odor" below that.

***Make sure that you everything is in between the yellow dashes and make sure that you include the dimensions in the file. Please give this to me in a vector format

IF YOU CAN INCLUDE YOUR EMAIL SO I CAN IMMEDIATELY CONTACT YOU AS SOON AS YOU ARE DONE. I would like to get this done and pay you as soon as possible.

Below are all the necessary files that you should need.

Target Market(s)

Wealthier clients

Industry/Entity Type

It Company

Font styles to use
Sans Serif

Colors
ec1f27
000000
ffffff

Requirements
Must have
• Canadian Flag
• Company Logo located in the files
• File must be in vector format
• Dimensions must be seen
• Everything must be with dashed yellow lines
• ZELPA and BRELLANTIX Logos
Nice to have
• ZELPA and BRELLANTIX symbols in black
Should not have
• Anything outside of the yellow dashed lines

```html
<!DOCTYPE html>
<html lang="en">
<head>
<meta charset="utf-8">
<title>Harbourline Shelter – Canopy Triangle Panel</title>
<link rel="stylesheet" href="https://fonts.googleapis.com/css2?family=Montserrat:wght@700&family=Tinos&display=swap">
<style>
  :root {
    --canopy-red: #e1001e;
    --white: #ffffff;
    --ink: #1a1a1a;
    --safe-line: #f5e100;
    --fold-line: #3a8fe0;
    --paper: #ffffff;
  }
  html, body {
    margin: 0;
    padding: 0;
    overflow: hidden;
    background: var(--paper);
  }
  .canvas {
    width: 1200px;
    height: 900px;
    position: relative;
    overflow: hidden;
    background: var(--paper);
  }
  .panel-drawing {
    display: block;
    width: 1200px;
    height: 900px;
  }
  .canopy-fill { fill: var(--canopy-red); }
  .safe-area {
    fill: none;
    stroke: var(--safe-line);
    stroke-width: 1.6;
    stroke-dasharray: 5 4;
  }
  .fold-line {
    stroke: var(--fold-line);
    stroke-width: 1.6;
    stroke-dasharray: 4 3;
  }
  .leaf-area { fill: var(--white); }
  .brand-name {
    font-family: "Montserrat", sans-serif;
    font-weight: 700;
    fill: var(--white);
  }
  .brand-name--main { font-size: 96px; }
  .brand-name--sub { font-size: 22px; }
  .dimension-line {
    stroke: var(--ink);
    stroke-width: 1;
    fill: none;
  }
  .dimension-label {
    font-family: "Tinos", serif;
    font-size: 52px;
    fill: var(--ink);
  }
</style>
</head>
<body>
<main class="canvas">
  <svg class="panel-drawing" viewBox="0 0 1200 900" xmlns="http://www.w3.org/2000/svg">
    <!-- Canopy triangle panel -->
    <g class="canopy-panel">
      <path class="canopy-fill" d="M245,683 Q520,470 695,150 Q870,470 1145,683 L1145,687 L245,687 Z"/>
      <path class="safe-area" d="M282,673 Q540,465 695,175 Q850,465 1112,673 Z"/>
      <line class="fold-line" x1="620" y1="277" x2="770" y2="277"/>

      <rect class="leaf-area" x="667" y="198" width="58" height="70" rx="6"
            role="img" aria-label="White maple leaf emblem at the top of the canopy"/>

      <text class="brand-name brand-name--main" x="433" y="615" textLength="542" lengthAdjust="spacingAndGlyphs">MARVELLO</text>
      <text class="brand-name brand-name--sub" x="652" y="643" textLength="330" lengthAdjust="spacing">DETAILING</text>
    </g>

    <!-- Height dimension -->
    <g class="dimension dimension--height">
      <line class="dimension-line" x1="133" y1="141" x2="220" y2="141"/>
      <line class="dimension-line" x1="138" y1="686" x2="232" y2="686"/>
      <line class="dimension-line" x1="183" y1="141" x2="183" y2="686"/>
      <text class="dimension-label" x="175" y="436" text-anchor="middle">184cm</text>
    </g>

    <!-- Width dimension -->
    <g class="dimension dimension--width">
      <line class="dimension-line" x1="236" y1="692" x2="236" y2="787"/>
      <line class="dimension-line" x1="1147" y1="686" x2="1147" y2="773"/>
      <line class="dimension-line" x1="236" y1="737" x2="1147" y2="737"/>
      <text class="dimension-label" x="685" y="735" text-anchor="middle">304cm</text>
    </g>
  </svg>
</main>
</body>
</html>
```